Pub/Bar snack and nibbles packaging

What we want:
We require professional packaging design for our jerky range.

About us and why we're here:
We're a husband and wife team from a small town who has been supplying artesian dried meats to local pubs/bars in outback Australia. Through word of mouth our volume has been growing steadily these few years. We seek someone who can assist provide a packaging range that best represents what great products my wife and I have been producing. And ultimately, a packaging that this product deserves. We have attached pictures of bar/pubs to give an idea of where our product is typically placed.

Target Market(s)

Target market:
Our customers are patrons of country motels / pubs and convenience stores. Our jerky goes particularly well with a cold beer.

Industry/Entity Type

It Professional

Requirements
Must have
• Specifics:
• Business Name: Quandong Meats. Artisan Style.
• Product: Beef Chunks (we have 4 different flavours original, spicy, honey, pepper. The design should be easily changeable to accomodate different flavours)
• Description: Made from 100% Australian Beef
• Typography: We have attached some fonts for inspiration (e.g., copper heron, other alcohol brands)
• Packet Size: 110mm (w) x 170mm (l)
• We also require the back of the packaging designed as well. That information will be provided to the winning designer chosen.
Nice to have
• Design Concept:
• The design should tell a story which features an outback or bush setting. We have provided a few examples for inspiration (e.g., jackaroo walking with working dog, on a horse, swagman camping) or come up with your own. We will decide the final design based on the story that we can most related to.
Should not have
• We do not want any photo images on this design, illustrations and text only.

```html
<!DOCTYPE html>
<html lang="en">
<head>
<meta charset="utf-8">
<title>Quandong Meats – Spicy Beef Chunks</title>
<link rel="stylesheet" href="https://fonts.googleapis.com/css2?family=Roboto+Slab:wght@700&family=Merriweather:ital,wght@0,300;0,700;1,700&display=swap">
<style>
  :root {
    --kraft: #c9a680;
    --kraft-dark: #b8946c;
    --ember: #f05623;
    --bark: #5a2c0d;
    --scene-tone: #a98260;
  }
  * { margin: 0; padding: 0; box-sizing: border-box; }
  html, body { width: 777px; height: 1200px; overflow: hidden; }
  body {
    background: radial-gradient(ellipse at 50% 40%, #cfac86 0%, var(--kraft) 60%, var(--kraft-dark) 100%);
    position: relative;
    color: var(--bark);
  }
  .brand-panel {
    position: absolute;
    left: 39px; top: 44px;
    width: 693px; height: 366px;
    background: var(--ember);
    display: flex; flex-direction: column;
    align-items: center; justify-content: center;
  }
  .brand-name {
    font-family: "Roboto Slab", serif;
    font-weight: 700;
    font-size: 112px;
    line-height: 1.02;
    text-align: center;
    color: var(--bark);
    letter-spacing: -2px;
    transform: scaleX(0.82);
  }
  .rule-pair {
    position: absolute;
    left: 39px; width: 693px;
    height: 15px;
    border-top: 4px solid var(--bark);
    border-bottom: 4px solid var(--bark);
  }
  .rule-pair--top { top: 422px; }
  .rule-pair--mid { top: 1042px; }
  .rule-pair--bottom { top: 1124px; }
  .tagline {
    position: absolute;
    top: 485px; left: 0; width: 100%;
    text-align: center;
    font-family: "Merriweather", serif;
    font-style: italic;
    font-weight: 700;
    font-size: 36px;
  }
  .scene {
    position: absolute;
    left: 80px; top: 610px;
    width: 607px; height: 290px;
    background: radial-gradient(ellipse at 50% 55%, var(--scene-tone) 0%, rgba(169,130,96,0.5) 55%, rgba(201,166,128,0) 80%);
  }
  .flavour-ribbon {
    position: absolute;
    left: 258px; top: 954px;
    width: 260px; height: 62px;
  }
  .flavour-label {
    position: absolute;
    left: 305px; top: 956px;
    width: 170px; height: 58px;
    display: flex; align-items: center; justify-content: center;
    font-family: "Merriweather", serif;
    font-weight: 700;
    font-size: 27px;
    color: var(--bark);
  }
  .description {
    position: absolute;
    top: 1075px; left: 0; width: 100%;
    text-align: center;
    font-family: "Merriweather", serif;
    font-weight: 300;
    font-size: 27px;
  }
</style>
</head>
<body>
  <header class="brand-panel">
    <h1 class="brand-name">Quandong<br>Meats</h1>
  </header>

  <div class="rule-pair rule-pair--top"></div>

  <p class="tagline">Artisan Style</p>

  <div class="scene" role="img" aria-label="Silhouette illustration of a bush camp: pine trees, distant mountains, a gum tree, a tent, and a swagman in a hat warming his hands at a campfire"></div>

  <svg class="flavour-ribbon" viewBox="0 0 260 62" aria-hidden="true">
    <polygon points="0,8 50,8 50,52 0,52 14,30" fill="var(--ember)"/>
    <polygon points="210,8 260,8 246,30 260,52 210,52" fill="var(--ember)"/>
    <rect x="47" y="2" width="170" height="58" fill="var(--ember)"/>
  </svg>
  <p class="flavour-label">Spicy</p>

  <div class="rule-pair rule-pair--mid"></div>

  <p class="description">Made from 100% Australian Beef</p>

  <div class="rule-pair rule-pair--bottom"></div>
</body>
</html>
```